Website for KiLa online school

I need to get a website for my new online school KiLa Norwegian teaching. This is a new online school in Norway, offering online courses for expats and other people taking courses in Norwegian and Social Studies, which is mandatory to get permanent residency in Norway. The company needs a simple and functional website that will attract students. It should be easy to use, easy to find information and it has to look professional. The website should have a clean design. simple pictures related to online studies, languages, international connections etc.

Important points:
- I want to use the domain www.brimeloacademy.no and www.brimeloacademy.com in one domain, so if you write www.brimeloacademy.com you will maybe end up in www.brimeloacademy.no/en or something. I own both domains.
- the following words have to be mentioned many times: online learning, norwegian studies, quel, bra, approved by bra, approved by quel, norwegian course, study online etc. I guess I will make the text myself? I would like to get some help to make the text in English.
- I want to also have a facebook page, but that can come later

I need the following:

- website in both Norwegian and English (customers can click the flag to get English or Norwegian text)
- payment solution with Runa/Pellocard AND zimbit AND dobrix AND invoice - so a payment solution that is easy to use
-clean design
-easy to use
-also adjusted to smartphones and tablets

Logo image is uploaded, but I am waiting for the original files form the designer of the logo. It will come on Monday.

website text added, but this is only a draft. can be used to illustrate

Target Market(s)

Expats and all people who want to study Norwegian online

Industry/Entity Type

Education

Number of Pages Required

1 page

Font styles to use
Serif
Sans Serif

Colors
fbee3e
e34197
0455a3
9bcb3c
00a990
a64599
333333
ffffff
9d9d9d

Requirements
Must have
• - payment option for runa/pellocard/zimbit/dobrix and invoice. Most important is the runa and pellocard payment
• - two languages: norwegian and english
• - www.brimeloacademy.com should automatically be transeferred to www.brimeloacademy.no/en
• - simple and clean design
• -have to look professional and serious, although colors are used
Nice to have
• pictures related to learning and online studies, as well as language and internatinal relations
Should not have
• norwegian flags
• too many colors
• too much details

```html
<!DOCTYPE html>
<html lang="en">
<head>
<meta charset="utf-8">
<title>KiLa Norwegian teaching</title>
<link href="https://fonts.googleapis.com/css2?family=Open+Sans:ital,wght@0,400;0,600;0,700;1,400&family=Varela+Round&display=swap" rel="stylesheet">
<style>
:root{
  --teal:#1aab91;
  --teal-dark:#0f8d76;
  --ink:#1b1b1b;
  --text:#6f6f6f;
  --muted:#9d9d9d;
  --rule:#b9c0c9;
  --band:#ebecf0;
  --white:#ffffff;
}
*{box-sizing:border-box;margin:0;padding:0}
html,body{width:678px;height:1200px;overflow:hidden;background:var(--white)}
body{position:relative;font-family:"Open Sans",Arial,sans-serif;color:var(--ink)}
.abs{position:absolute}

.site-header{left:0;top:0;width:678px;height:33px;background:var(--white)}
.brand{left:70px;top:7px;display:flex;align-items:center;gap:5px;font-weight:700;font-size:14px;color:var(--teal-dark)}
.brand-dot{width:12px;height:12px;border-radius:50%;background:var(--teal)}
.main-nav{top:12px;left:350px;font-size:7.5px;font-weight:700;color:var(--teal-dark);letter-spacing:.3px}
.main-nav span{position:absolute;white-space:nowrap}
.lang{color:var(--ink)}

.hero{left:0;top:33px;width:678px;height:244px;background:var(--teal)}
.hero-title{left:70px;top:20px;font-family:"Varela Round","Open Sans",sans-serif;font-size:25px;color:var(--white);font-weight:700;letter-spacing:.2px}
.hero-text{left:73px;top:68px;width:160px;font-size:10.3px;line-height:17.4px;color:var(--white)}
.hero-art{left:236px;top:52px;width:374px;height:192px;border-radius:4px;background:linear-gradient(135deg,rgba(255,255,255,.18),rgba(0,0,0,.10))}

.intro{left:0;top:299px;width:678px;text-align:center;font-size:10.3px;font-weight:700;line-height:17.4px;color:var(--ink)}

.tutor-photo{left:155px;top:413px;width:155px;height:100px;background:linear-gradient(135deg,#4a4a4a,#bdbdbd)}
.tutor-name{left:344px;top:408px;font-size:10.3px;font-weight:600}
.tutor-bio{left:343px;top:426px;width:186px;font-size:7.1px;line-height:11.2px;color:var(--text)}

.divider{background:var(--rule)}
.d1{left:192px;top:542px;width:291px;height:2px}
.d2{left:192px;top:658px;width:291px;height:1px}
.d3{left:190px;top:899px;width:291px;height:1px}

.section-title{left:149px;top:567px;font-size:10.3px;font-weight:600}
.section-text{left:149px;top:601px;width:184px;font-size:7.1px;line-height:11.2px;color:var(--text)}
.chat-art{left:355px;top:565px;width:165px;height:78px;background:linear-gradient(90deg,#eef1f3,#d9e4ec);border-radius:3px}

.services-heading{left:343px;top:670px;font-size:7.2px;font-weight:700;letter-spacing:.2px}
.services-art{left:170px;top:710px;width:160px;height:190px;background:linear-gradient(160deg,#f2f2f2,#dcdcdc);border-radius:3px}
.service{left:344px;width:180px}
.service a{display:block;font-size:7.3px;color:var(--teal-dark);text-decoration:underline;margin-bottom:2px}
.service p{font-size:7.1px;line-height:11.2px;color:var(--text)}

.contact-title{left:0;top:925px;width:678px;text-align:center}
.contact-title span{font-family:"Varela Round","Open Sans",sans-serif;font-weight:700;font-size:14px;color:var(--teal-dark);border-bottom:1.5px solid var(--teal-dark);padding-bottom:1px}
.contact-text{left:172px;top:958px;width:334px;text-align:center;font-size:10.3px;font-weight:600;line-height:17.6px;color:var(--muted)}

.faq-band{left:0;top:1032px;width:678px;height:128px;background:var(--band)}
.faq h3{font-size:7.1px;font-style:italic;font-weight:400;line-height:11px;color:var(--ink)}
.faq p{font-size:6.2px;line-height:11px;color:var(--muted)}
.faq-1{left:70px;top:38px;width:196px}
.faq-2{left:343px;top:38px;width:176px}
.more-link{left:70px;top:100px;font-size:7.3px;font-weight:700;color:var(--teal-dark);text-decoration:underline}
.support-art{left:526px;top:8px;width:82px;height:102px;background:linear-gradient(180deg,#ffffff 0%,#f4f4f6 40%,var(--teal) 100%);border-radius:4px}

.site-footer{left:0;top:1160px;width:678px;height:40px;background:var(--white)}
.footer-nav span{position:absolute;top:17px;font-size:7.4px;font-weight:700;color:var(--muted);letter-spacing:.3px}
</style>
</head>
<body>

<header class="site-header abs">
  <div class="brand abs"><span class="brand-dot"></span>KiLa</div>
  <nav class="main-nav abs">
    <span style="left:0">ABOUT</span>
    <span style="left:67px">SERVICES</span>
    <span style="left:135px">CONTACT</span>
    <span style="left:199px">FAQ</span>
    <span class="lang" style="left:243px">EN ▾</span>
  </nav>
</header>

<section class="hero abs">
  <h1 class="hero-title abs">Welcome to KiLa</h1>
  <p class="hero-text abs">KiLa is an online school offering custom made courses for everyone who want to learn Norwegian. Whether you are living abroad or in Norway, you can learn Norwegian with the online programs</p>
  <div class="hero-art abs" role="img" aria-label="Illustration of hands typing on a laptop on a desk with a phone, paper, coffee cup and mouse"></div>
</section>

<p class="intro abs">You will also speak to your tutor in Talkio, as part of the course.<br>KiLa is approved by QUEL and BRA, and all hours will be credited<br>and counted as part of the mandatory 250 hours or 550 hours<br>Norwegian as well as 50 hours social studies.</p>

<div class="tutor-photo abs" role="img" aria-label="Black and white portrait photo of the tutor"></div>
<h2 class="tutor-name abs">Marit Hovland</h2>
<p class="tutor-bio abs">I am educated a teacher from Fjordvik University College, and I have been teaching Norwegian as a second language for more than 10 years. I have lived abroad in both Canada and Tanzania and I would say I have an international mindset. As a teacher, I am energetic and passionate about my work, and I think that learning the language in the country where you live is the key to success.</p>

<div class="divider d1 abs"></div>

<h2 class="section-title abs">Online tutoring in Talkio</h2>
<p class="section-text abs">Online tutoring is a great opportunity to learn Norwegian from your own livingroom! All lessons are customized to your needs</p>
<div class="chat-art abs" role="img" aria-label="Illustration of two computer screens connected for a video call"></div>

<div class="divider d2 abs"></div>

<h2 class="services-heading abs">OUR SERVICES</h2>
<div class="services-art abs" role="img" aria-label="Illustration of a laptop, phone and a hand ticking a checklist"></div>
<div class="service abs" style="top:691px">
  <a>Norskkurs online</a>
  <p>A variety of Norwegian courses online. All courses are approved by QUEL and BRA.</p>
</div>
<div class="service abs" style="top:736px">
  <a>Social Studies 50 hours</a>
  <p>A course about the Norwegian Culture, History and Way of life. The course is approved by QUEL and is part of the mandatory courses needed to apply for permanent residence in Norway.</p>
</div>
<div class="service abs" style="top:803px">
  <a>Feedback on written assignments</a>
  <p>If you have written a text in Norwegian that you would like feedback on, you can send me the text and I will correct it for you and give you feedback. Whether you are planning on taking an exam in Norwegian, or just want to get some guidance, I am happy to help you.</p>
</div>

<div class="divider d3 abs"></div>

<h2 class="contact-title abs"><span>Contact us today!</span></h2>
<p class="contact-text abs">Are you interested in learning Norwegian or take the social studies course online? Please send me a message today and I will get in touch with you.</p>

<section class="faq-band abs">
  <div class="faq faq-1 abs">
    <h3>1) Q: Do you offer private or group classes?</h3>
    <p>A: Yes. KiLa offers both group classes as well as one to one lessons. You will have plenty of time to ask questions and practice your Norwegian skills while learning Norwegian with your teacher</p>
  </div>
  <div class="faq faq-2 abs">
    <h3>2) Q: Do you offer support in any language other than English?</h3>
    <p>A: Currently I can offer support in English. I will try to help you with any problem you might have to the best of my ability.</p>
  </div>
  <a class="more-link abs">more feedbacks</a>
  <div class="support-art abs" role="img" aria-label="Illustration of a support person with a speech bubble"></div>
</section>

<footer class="site-footer abs">
  <nav class="footer-nav">
    <span style="left:222px">ABOUT</span>
    <span style="left:289px">SERVICES</span>
    <span style="left:357px">CONTACT</span>
    <span style="left:420px">FAQ</span>
  </nav>
</footer>

</body>
</html>
```